Business Card Design

We need a design for business cards for our company. We have a logo. We teach EMT's and we are based out of Virginia. The information that will need to add would be, name, title, phone number, email, address. On the back of the business card would be "We help you, help others"

Target Market(s)

People that want to become EMT's

Colors

Designer to choose colors to be used in the design.

Requirements
Must have
• company logo

```html
<!DOCTYPE html>
<html lang="en">
<head>
<meta charset="utf-8">
<title>Medic Path Academy — Business Card</title>
<link href="https://fonts.googleapis.com/css2?family=Montserrat:wght@500;600;700&family=Open+Sans:wght@700&display=swap" rel="stylesheet">
<style>
  :root {
    --stage: #1c1c1e;
    --card-navy: #2b3641;
    --card-navy-light: #334150;
    --brand-red: #e4223f;
    --wave-grey: #7f8d98;
    --text-grey: #9aa4ad;
    --text-white: #ffffff;
  }
  * { box-sizing: border-box; margin: 0; padding: 0; }
  html, body {
    width: 1200px; height: 1200px; overflow: hidden;
    background: var(--stage);
  }
  .sheet {
    position: relative; width: 1200px; height: 1200px;
    display: flex; flex-direction: column; align-items: center; justify-content: center; gap: 44px;
  }
  .card {
    position: relative; width: 900px; height: 514px; overflow: hidden;
    background: linear-gradient(160deg, var(--card-navy-light), var(--card-navy) 60%);
    box-shadow: 0 12px 30px rgba(0,0,0,.5);
  }
  /* back side */
  .card-back { display: flex; align-items: center; justify-content: center; }
  .tagline {
    font-family: "Open Sans", sans-serif; font-weight: 700; font-size: 50px;
    letter-spacing: 0.5px; white-space: nowrap;
  }
  .tagline .quote-open, .tagline .lead { color: var(--brand-red); }
  .tagline .rest, .tagline .quote-close { color: var(--text-grey); }
  .tagline .quote-open, .tagline .quote-close { font-size: 60px; vertical-align: 0.15em; }

  /* front side */
  .waves { position: absolute; inset: 0; width: 100%; height: 100%; }
  .brand {
    position: absolute; left: 48px; top: 70px;
    display: flex; align-items: center; gap: 14px;
  }
  .brand-dot { width: 30px; height: 30px; border-radius: 50%; background: var(--brand-red); }
  .brand-name {
    font-family: "Montserrat", sans-serif; font-weight: 700; font-size: 40px;
    color: var(--brand-red); letter-spacing: 0.5px;
  }
  .person {
    position: absolute; right: 48px; top: 150px; text-align: right;
    font-family: "Montserrat", sans-serif;
  }
  .person-name { font-weight: 700; font-size: 27px; color: var(--brand-red); letter-spacing: 1px; }
  .person-title { font-weight: 600; font-size: 18px; color: var(--text-grey); letter-spacing: 1.5px; margin-top: 2px; }
  .contact {
    position: absolute; right: 44px; bottom: 42px; text-align: right;
    font-family: "Montserrat", sans-serif; font-weight: 500; font-size: 21px;
    color: var(--text-white); line-height: 1.45;
  }
  .contact-row { display: flex; justify-content: flex-end; align-items: center; gap: 10px; }
  .contact-row svg { width: 24px; height: 24px; flex: none; }
  .contact-address { padding-right: 34px; }
</style>
</head>
<body>
<main class="sheet">
  <section class="card card-back" aria-label="Card back">
    <p class="tagline"><span class="quote-open">“</span><span class="lead">We help you,</span> <span class="rest">help others</span><span class="quote-close">”</span></p>
  </section>

  <section class="card card-front" aria-label="Card front">
    <svg class="waves" viewBox="0 0 900 514" preserveAspectRatio="none" aria-hidden="true">
      <path d="M0,205 C180,270 330,330 560,300 C700,282 800,265 900,262 L900,292 C800,296 700,312 560,330 C330,360 170,310 0,245 Z" fill="var(--wave-grey)"/>
      <path d="M0,268 C170,330 330,368 560,345 C700,331 800,322 900,330 L900,356 C800,350 700,356 560,368 C330,390 160,360 0,300 Z" fill="var(--wave-grey)"/>
      <path d="M0,352 C250,318 520,300 680,318 C780,330 850,360 900,412 L900,514 L0,514 Z" fill="var(--brand-red)"/>
    </svg>

    <div class="brand">
      <span class="brand-dot"></span>
      <span class="brand-name">MEDIC PATH ACADEMY</span>
    </div>

    <div class="person">
      <p class="person-name">JORDAN ELLIS</p>
      <p class="person-title">MANAGING DIRECTOR</p>
    </div>

    <address class="contact" style="font-style:normal">
      <div class="contact-row">
        <span>555 013 2840</span>
        <svg viewBox="0 0 24 24" aria-hidden="true"><circle cx="12" cy="12" r="10.5" fill="none" stroke="#fff" stroke-width="1.6"/><path d="M8.5 7.5c.6-.6 1.3-.5 1.6.1l.8 1.6c.2.5 0 1-.4 1.3l-.6.5c.5 1.3 1.6 2.4 2.9 2.9l.5-.6c.3-.4.8-.6 1.3-.4l1.6.8c.6.3.7 1 .1 1.6-1 1-2.6 1.1-4.3 0-1.5-1-2.8-2.3-3.8-3.8-1.1-1.7-1-3.3 0-4.3z" fill="#fff"/></svg>
      </div>
      <div class="contact-row">
        <span>hello@medicpathacademy.com</span>
        <svg viewBox="0 0 24 24" aria-hidden="true"><circle cx="12" cy="12" r="10.5" fill="none" stroke="#fff" stroke-width="1.6"/><rect x="6.5" y="8.5" width="11" height="7.5" rx="1" fill="#fff"/><path d="M6.8 9l5.2 4 5.2-4" fill="none" stroke="var(--brand-red)" stroke-width="1.3"/></svg>
      </div>
      <div class="contact-address">88 Harbor Street, Suite 210<br>Riverton, VA 23401</div>
    </address>
  </section>
</main>
</body>
</html>
```